Print Ad for Pilates Studio

I need a full color 1/4 page ad (size 5" tall x 3 3/4" wide) that includes our logo at top with this text:
Intro Specials for New Students:
3 Private Sessions for only $150 (normally $75/session)
3 Group Reformer Classes for $49 (normally $35/class)
5 Bootcamp Classes for only $29 (normally $15/class0
and might include the tree graphic, and the three small logos (QRN, Green-certified and Top Pick) at bottom plus our phone number really big
555-214-3096 and e-mail MarissaTolvane@mailbrook.example and website www.steadycorefit.example
Should look enticing and CLEAN

Target Market(s)

Older affluent market

Industry/Entity Type

Group

Requirements
Must have
• Clean lines
• Bold
• Classy
• some space
• Makes you want to take action now
Nice to have
• photo of people doing pilates
• Bold color like yellow, green, burgundy

```html
<!DOCTYPE html>
<html lang="en">
<head>
<meta charset="utf-8">
<title>Steady Core – Intro Specials Ad</title>
<link rel="stylesheet" href="https://fonts.googleapis.com/css2?family=Questrial&family=Roboto+Condensed:wght@400;700&family=Roboto:wght@700&display=swap">
<style>
  :root {
    --green-deep: #1f4a1d;
    --green-band: #234f22;
    --green-mid: #3f7a35;
    --green-light: #6fa152;
    --green-logo: #4d7f2e;
    --gold: #c79a3a;
    --gold-light: #e2b65a;
    --sky: #f1f3f2;
    --white: #ffffff;
    --text-light: #f4f6f1;
  }
  * { box-sizing: border-box; margin: 0; padding: 0; }
  html, body { width: 901px; height: 1200px; overflow: hidden; background: var(--white); }
  .ad {
    position: relative;
    width: 901px;
    height: 1200px;
    overflow: hidden;
    font-family: "Roboto Condensed", "Arial Narrow", sans-serif;
    color: var(--text-light);
  }
  .ad-backdrop { position: absolute; inset: 0; }

  .brand { position: absolute; left: 30px; top: 32px; display: flex; align-items: center; gap: 18px; }
  .brand-mark { width: 58px; height: 58px; border-radius: 50%; border: 7px solid var(--gold); }
  .brand-name {
    font-family: "Questrial", sans-serif;
    font-size: 70px; line-height: 1; color: var(--green-logo); letter-spacing: -1px;
  }
  .brand-tagline {
    position: absolute; left: 241px; top: 124px;
    width: 395px; height: 32px; border-radius: 4px;
    background: var(--green-logo); color: var(--white);
    font-family: "Roboto", sans-serif; font-weight: 700; font-size: 22px;
    display: flex; align-items: center; justify-content: center; letter-spacing: .3px;
  }

  .headline {
    position: absolute; left: 40px; top: 298px;
    font-family: "Questrial", sans-serif; font-size: 47px; line-height: 72px;
    color: var(--white); letter-spacing: 1px;
  }

  .offer { position: absolute; left: 32px; width: 560px; }
  .offer-title { font-size: 34px; font-weight: 700; white-space: nowrap; }
  .offer-title .for { font-size: 27px; font-weight: 400; }
  .offer-title .price { font-size: 44px; font-weight: 700; color: var(--gold-light); }
  .offer-note { margin: 6px 0 0 166px; font-size: 29px; font-weight: 400; }
  .offer--private { top: 548px; }
  .offer--reformer { top: 686px; }
  .offer--bootcamp { top: 824px; }

  .call { position: absolute; left: 40px; top: 966px; white-space: nowrap; display: flex; align-items: baseline; gap: 12px; }
  .call-label { font-size: 38px; }
  .call-number { font-size: 72px; font-weight: 700; letter-spacing: 1px; }

  .contact { position: absolute; left: 62px; top: 1084px; font-family: "Roboto", sans-serif; font-weight: 700; font-size: 27px; line-height: 40px; letter-spacing: .4px; }

  .badges { position: absolute; left: 550px; top: 1063px; display: flex; gap: 12px; }
  .badge { width: 106px; height: 102px; border-radius: 4px; }
  .badge--green { background: var(--white); }
  .badge--cert { background: linear-gradient(#ffffff 0 62%, #6f8fb8 62%); }
  .badge--award { width: 92px; background: linear-gradient(160deg, #2c5a9e, #163a76); }
</style>
</head>
<body>
<main class="ad">
  <svg class="ad-backdrop" width="901" height="1200" viewBox="0 0 901 1200" aria-hidden="true">
    <defs>
      <linearGradient id="field" x1="0" y1="0" x2="0.3" y2="1">
        <stop offset="0" stop-color="#2f5f2a"/>
        <stop offset="0.45" stop-color="#5f9445"/>
        <stop offset="1" stop-color="#2e5f2a"/>
      </linearGradient>
      <linearGradient id="top" x1="0" y1="0" x2="0" y2="1">
        <stop offset="0" stop-color="#ffffff"/>
        <stop offset="1" stop-color="#e6e8e7"/>
      </linearGradient>
      <linearGradient id="photo" x1="0" y1="0" x2="1" y2="1">
        <stop offset="0" stop-color="#f2f1ee"/>
        <stop offset="0.5" stop-color="#d8c2a8"/>
        <stop offset="1" stop-color="#9c8670"/>
      </linearGradient>
      <radialGradient id="tree" cx="0.55" cy="0.4" r="0.6">
        <stop offset="0" stop-color="#2f6a2a" stop-opacity="0.9"/>
        <stop offset="1" stop-color="#2f6a2a" stop-opacity="0"/>
      </radialGradient>
    </defs>
    <rect width="901" height="1200" fill="url(#top)"/>
    <rect y="198" width="901" height="1002" fill="url(#field)"/>
    <rect y="193" width="470" height="6" fill="var(--gold)"/>
    <g role="img" aria-label="Tree with leafy branches spreading across the right side">
      <ellipse cx="770" cy="640" rx="220" ry="260" fill="url(#tree)"/>
      <rect x="795" y="700" width="40" height="320" fill="#2a5a26" opacity="0.7"/>
    </g>
    <g role="img" aria-label="Photo of three women exercising on Pilates reformers in a bright studio">
      <circle cx="745" cy="320" r="295" fill="url(#photo)"/>
    </g>
    <path d="M450 330 A295 295 0 0 0 600 590" fill="none" stroke="var(--gold)" stroke-width="6"/>
    <path d="M0 548 H600 L582 640 H0 Z" fill="var(--green-band)"/>
    <path d="M0 686 H600 L582 778 H0 Z" fill="var(--green-band)"/>
    <path d="M0 824 H600 L582 916 H0 Z" fill="var(--green-band)"/>
    <rect y="652" width="556" height="4" fill="#1a3a19" opacity="0.6"/>
    <rect y="790" width="556" height="4" fill="#1a3a19" opacity="0.6"/>
    <rect y="928" width="556" height="4" fill="#1a3a19" opacity="0.6"/>
    <path d="M582 640 L600 548 L588 640 Z" fill="var(--gold)"/>
    <path d="M582 778 L600 686 L588 778 Z" fill="var(--gold)"/>
    <path d="M582 916 L600 824 L588 916 Z" fill="var(--gold)"/>
    <path d="M0 1055 C300 1060 650 1040 901 960 V1200 H0 Z" fill="var(--green-deep)"/>
    <path d="M0 1052 C300 1058 650 1036 901 956 V966 C650 1046 300 1068 0 1066 Z" fill="var(--gold)"/>
  </svg>

  <header class="brand">
    <span class="brand-mark"></span>
    <span class="brand-name">Steady Core</span>
  </header>
  <div class="brand-tagline">Pilates &amp; Flowline Studio</div>

  <h1 class="headline">Intro<br>Specials for<br>New Students:</h1>

  <section class="offer offer--private">
    <p class="offer-title">3 Private Sessions <span class="for">for only</span> <span class="price">$150</span></p>
    <p class="offer-note">(Normally $ 75/Session)</p>
  </section>
  <section class="offer offer--reformer">
    <p class="offer-title">3 Group Reformer <span class="for">for only</span> <span class="price">$49</span></p>
    <p class="offer-note">(Normally $ 35/Session)</p>
  </section>
  <section class="offer offer--bootcamp">
    <p class="offer-title">5 Bootcamp Classes <span class="for">for only</span> <span class="price">$29</span></p>
    <p class="offer-note">(Normally $ 15/Class)</p>
  </section>

  <p class="call"><span class="call-label">Call US :</span><span class="call-number">555-214-3096</span></p>

  <address class="contact" style="font-style:normal">
    MarissaTolvane@mailbrook.example<br>
    www.steadycorefit.example
  </address>

  <div class="badges">
    <span class="badge badge--green" role="img" aria-label="Green business certification badge"></span>
    <span class="badge badge--cert" role="img" aria-label="QRN Pilates certification badge"></span>
    <span class="badge badge--award" role="img" aria-label="Top Pick award badge"></span>
  </div>
</main>
</body>
</html>
```